We need 3 A2 posters similar look but different enough to be eye catching when changed.

We are a healthcare centre that requires 3 A2 posters - simple, similar but different background colours. These posters will be used within our business to promote services we provide to our clients.

The design should include our logo(attached), a large header and a large section in the middle of the poster to promote the event. We need a blank text box (which WE can insert text to advertise), and 1 image to advertise the event. Please note, we do not need you to choose an image we simply would like you to place a demo to give us an idea of where it should sit.

We want to use the bubble design (attached) as a background and the company colours pink, orange and blue - as on our website. Attached is a copy of our logo and background bubble effect. You can also refer to our website - www.tallowbrookwellness.com.au for more inspiration.

Just to reiterate, these posters should be simple, different but have a uniform feel. They should have an empty middle section that can be edited to add text and a space for an eye catching title and matching image.

Our services include Chiropractic, Podiatry, Nutrition, Massage, Yoga, Pilates and Specialised rehabilitation classes.

Reason: Hi designers, I know we are all busy but I really need more designs from the designers I invited to this project and look forward to receiving more designs. Any questions please let me know. Regards, Marlene

Reason: Hi all Increased the budget Regards Marlene

Target Market(s)

Corporate Sydney City office workers

Industry/Entity Type

Healthcare

Requirements
Must have
• logo and company colours
section in the middles that can be edited to add text
Space allocated for image placement
Catchy title/header

```html
<!DOCTYPE html>
<html lang="en">
<head>
<meta charset="utf-8">
<title>Tallowbrook Wellness – Poster Series</title>
<link rel="stylesheet" href="https://fonts.googleapis.com/css2?family=Jost:wght@400;500&family=Arimo:wght@700&display=swap">
<style>
  :root {
    --stage: #2b2b2b;
    --white: #ffffff;
    --brand-blue: #5a4fa3;
    --orange-light: #eba872;
    --orange-deep: #df6616;
    --lavender: #a7a4d6;
    --grey-light: #e3e3e3;
    --grey-mid: #c9c9c9;
    --pink-light: #ea9cc6;
    --pink-deep: #d23f8c;
    --title-orange: #e8741c;
    --title-purple: #4f479f;
    --title-pink: #d81b7b;
  }
  * { box-sizing: border-box; margin: 0; padding: 0; }
  html, body { width: 1200px; height: 690px; overflow: hidden; background: var(--stage); }
  .stage { position: relative; width: 1200px; height: 690px; }

  .poster { position: absolute; top: 146px; width: 298px; height: 422px; overflow: hidden; }
  .poster--peace { left: 122px; }
  .poster--back { left: 450px; }
  .poster--feel { left: 772px; }

  .brand-bar {
    position: absolute; left: 0; top: 0; width: 100%; height: 20px; z-index: 5;
    background: var(--brand-blue);
  }
  .brand-bar__name {
    position: absolute; left: 43px; top: 8px;
    font: 700 8px/10px "Arimo", sans-serif; color: var(--white); white-space: nowrap;
  }

  .backdrop { position: absolute; inset: 20px 0 0 0; }
  .poster--peace .backdrop { background: linear-gradient(180deg, var(--orange-light) 0%, #e9995a 45%, var(--orange-deep) 75%, #d95e12 100%); }
  .poster--back .backdrop { background: linear-gradient(180deg, var(--lavender) 0%, #b9b7dd 35%, var(--grey-mid) 60%, var(--grey-light) 100%); }
  .poster--feel .backdrop { background: linear-gradient(180deg, var(--pink-light) 0%, #e38bbb 50%, var(--pink-deep) 85%, #cc3a86 100%); }

  .bubble { position: absolute; background: var(--white); border-radius: 7px; }

  .photo { position: absolute; }
  .photo--yoga { left: 24px; top: 144px; width: 184px; height: 182px; border-radius: 0 0 10px 0;
    background: linear-gradient(160deg, #d9d4cf 0%, #8a7e76 40%, #3d6ea8 75%, #2a4f80 100%); }
  .photo--pilates { left: 113px; top: 117px; width: 185px; height: 185px;
    background: linear-gradient(150deg, #e8e2d6 0%, #cbbfa7 40%, #4aa3dc 60%, #3a3a3a 100%); }
  .photo--massage { left: 0; top: 112px; width: 298px; height: 246px;
    background: linear-gradient(150deg, #f6e6dc 0%, #d9a888 35%, #b9795a 60%, #f3ede8 100%); }

  .message-box { position: absolute; background: var(--white); border-radius: 10px; z-index: 3; }
  .headline { font: 400 17px/22px "Jost", sans-serif; }
  .poster--peace .message-box { left: 153px; top: 172px; width: 145px; height: 118px; padding: 16px 0 0 16px; }
  .poster--peace .headline { color: var(--title-orange); }
  .poster--back .message-box { left: 0; top: 150px; width: 135px; height: 112px; padding: 24px 0 0 12px; }
  .poster--back .headline { color: var(--title-purple); }
  .poster--feel .message-box { left: 0; top: 76px; width: 136px; height: 70px; padding: 10px 0 0 18px; }
  .poster--feel .headline { color: var(--title-pink); }
</style>
</head>
<body>
<main class="stage">

  <section class="poster poster--peace">
    <div class="brand-bar"><span class="brand-bar__name">Tallowbrook Wellness</span></div>
    <div class="backdrop" role="img" aria-label="Orange mosaic bubble background"></div>
    <div class="bubble" style="left:58px;top:60px;width:86px;height:80px"></div>
    <div class="bubble" style="left:20px;top:95px;width:80px;height:60px"></div>
    <div class="bubble" style="left:0;top:110px;width:40px;height:120px"></div>
    <div class="bubble" style="left:160px;top:80px;width:30px;height:30px"></div>
    <div class="bubble" style="left:191px;top:68px;width:10px;height:10px;border-radius:2px"></div>
    <div class="bubble" style="left:190px;top:118px;width:68px;height:80px"></div>
    <div class="bubble" style="left:24px;top:140px;width:216px;height:200px;border-radius:10px"></div>
    <div class="bubble" style="left:8px;top:302px;width:44px;height:44px"></div>
    <div class="bubble" style="left:110px;top:300px;width:130px;height:50px"></div>
    <div class="bubble" style="left:110px;top:320px;width:54px;height:58px"></div>
    <div class="bubble" style="left:162px;top:378px;width:24px;height:24px;border-radius:4px"></div>
    <div class="photo photo--yoga" role="img" aria-label="Photo placeholder: couple meditating in yoga pose"></div>
    <div class="message-box"><p class="headline">Look for some<br>peace in your<br>daily routine</p></div>
  </section>

  <section class="poster poster--back">
    <div class="brand-bar"><span class="brand-bar__name">Tallowbrook Wellness</span></div>
    <div class="backdrop" role="img" aria-label="Lavender to grey mosaic bubble background"></div>
    <div class="bubble" style="left:100px;top:98px;width:90px;height:60px"></div>
    <div class="bubble" style="left:155px;top:78px;width:22px;height:22px;border-radius:3px"></div>
    <div class="bubble" style="left:210px;top:64px;width:32px;height:32px"></div>
    <div class="bubble" style="left:222px;top:82px;width:76px;height:40px"></div>
    <div class="bubble" style="left:55px;top:132px;width:60px;height:40px"></div>
    <div class="bubble" style="left:0;top:122px;width:298px;height:190px;border-radius:0 0 10px 10px"></div>
    <div class="bubble" style="left:104px;top:300px;width:84px;height:40px"></div>
    <div class="photo photo--pilates" role="img" aria-label="Photo placeholder: woman stretching on a pilates reformer"></div>
    <div class="message-box"><p class="headline">Ease your<br>back pain<br>with Flexora</p></div>
  </section>

  <section class="poster poster--feel">
    <div class="brand-bar"><span class="brand-bar__name">Tallowbrook Wellness</span></div>
    <div class="backdrop" role="img" aria-label="Pink mosaic bubble background"></div>
    <div class="bubble" style="left:136px;top:40px;width:24px;height:24px;border-radius:4px"></div>
    <div class="bubble" style="left:56px;top:62px;width:80px;height:50px"></div>
    <div class="bubble" style="left:160px;top:70px;width:138px;height:60px"></div>
    <div class="photo photo--massage" role="img" aria-label="Photo placeholder: couple relaxing during a back massage"></div>
    <div class="bubble" style="left:0;top:340px;width:34px;height:34px"></div>
    <div class="bubble" style="left:48px;top:332px;width:78px;height:52px"></div>
    <div class="bubble" style="left:200px;top:316px;width:98px;height:78px"></div>
    <div class="message-box"><p class="headline">How do you<br>feel today?</p></div>
  </section>

</main>
</body>
</html>
```